TomasTunes poster

We need a poster to promote my live music show for hotels, Im playing for tourists in hotels in Palma de Mallorca, Spain, I would like to see the url of my web site in the poster www.tomastunes.es, in the web site you can see some of my music, thx

```html
<!DOCTYPE html>
<html lang="en">
<head>
<meta charset="utf-8">
<title>TomasTunes – Music Live Concert</title>
<link rel="stylesheet" href="https://fonts.googleapis.com/css2?family=Oswald:wght@700&family=Playfair+Display:ital,wght@0,400;1,400&family=Roboto+Condensed:wght@700&family=Montserrat:wght@600&display=swap">
<style>
  :root {
    --paper: #f1f3f5;
    --paper-light: #fbfcfc;
    --teal: #1f7a78;
    --teal-dark: #1d5c62;
    --green: #5fae3a;
    --crimson: #c92a5c;
    --plum: #8e2e63;
    --navy: #1e2b5c;
    --ink-teal: #0f4656;
    --yellow: #e6e64a;
  }
  * { margin: 0; padding: 0; box-sizing: border-box; }
  html, body { width: 927px; height: 1200px; overflow: hidden; }
  body { background: var(--paper); }
  .poster {
    position: relative;
    width: 927px;
    height: 1200px;
    overflow: hidden;
    background: linear-gradient(160deg, var(--paper) 0%, #e9ecef 45%, var(--paper-light) 100%);
  }
  .backdrop-curves { position: absolute; inset: 0; }
  .artwork {
    position: absolute;
    left: 40px;
    top: 220px;
    width: 470px;
    height: 740px;
    border-radius: 46% 54% 48% 52% / 40% 42% 58% 60%;
    background:
      radial-gradient(circle at 72% 62%, rgba(201,42,92,.75) 0%, rgba(201,42,92,0) 32%),
      radial-gradient(circle at 25% 85%, rgba(230,230,74,.8) 0%, rgba(230,230,74,0) 35%),
      radial-gradient(circle at 60% 92%, rgba(64,170,210,.7) 0%, rgba(64,170,210,0) 30%),
      linear-gradient(170deg, rgba(31,122,120,.85) 0%, rgba(95,174,58,.8) 50%, rgba(230,230,74,.55) 100%);
    opacity: .85;
    filter: blur(2px);
  }
  .brand {
    position: absolute;
    left: 520px;
    top: 150px;
    width: 280px;
    text-align: center;
    font-family: "Roboto Condensed", sans-serif;
    font-weight: 700;
    font-size: 54px;
    color: var(--teal-dark);
  }
  .headline { position: absolute; left: 0; top: 0; }
  .headline-music {
    position: absolute;
    left: 538px;
    top: 448px;
    font-family: "Oswald", sans-serif;
    font-weight: 700;
    font-size: 112px;
    line-height: 1;
    background: linear-gradient(90deg, var(--teal-dark) 0%, var(--teal) 45%, var(--crimson) 80%, var(--teal) 100%);
    -webkit-background-clip: text;
    background-clip: text;
    color: transparent;
  }
  .headline-live {
    position: absolute;
    left: 470px;
    top: 560px;
    font-family: "Playfair Display", serif;
    font-size: 192px;
    line-height: 1;
    background: linear-gradient(90deg, var(--crimson) 0%, var(--plum) 30%, var(--teal) 60%, var(--green) 85%, var(--teal) 100%);
    -webkit-background-clip: text;
    background-clip: text;
    color: transparent;
  }
  .headline-concert {
    position: absolute;
    left: 524px;
    top: 748px;
    font-family: "Montserrat", sans-serif;
    font-weight: 600;
    font-size: 32px;
    letter-spacing: 0.62em;
    color: var(--plum);
  }
  .event-date {
    position: absolute;
    left: 0;
    width: 927px;
    top: 924px;
    text-align: center;
    padding-left: 26px;
    font-family: "Playfair Display", serif;
    font-style: italic;
    font-size: 62px;
    color: var(--crimson);
  }
  .event-place {
    position: absolute;
    left: 0;
    width: 927px;
    top: 1004px;
    text-align: center;
    padding-left: 26px;
    font-family: "Roboto Condensed", sans-serif;
    font-weight: 700;
    font-size: 36px;
    color: var(--ink-teal);
  }
  .website {
    position: absolute;
    left: 0;
    width: 927px;
    top: 1070px;
    text-align: center;
    font-family: "Roboto Condensed", sans-serif;
    font-weight: 700;
    font-size: 52px;
    letter-spacing: 0.2em;
    color: var(--navy);
  }
</style>
</head>
<body>
  <main class="poster">
    <svg class="backdrop-curves" width="927" height="1200" viewBox="0 0 927 1200" aria-hidden="true">
      <circle cx="760" cy="880" r="330" fill="#ffffff" opacity=".55"/>
      <path d="M927 300 Q760 420 880 600" fill="none" stroke="#ffffff" stroke-width="6" opacity=".8"/>
      <path d="M0 700 Q300 660 560 780" fill="none" stroke="#ffffff" stroke-width="3" opacity=".7"/>
    </svg>

    <div class="artwork" role="img" aria-label="Colourful watercolour treble clef surrounded by scattered music notes"></div>

    <div class="brand">TomasTunes</div>

    <h1 class="headline">
      <span class="headline-music">MUSIC</span>
      <span class="headline-live">LIVE</span>
      <span class="headline-concert">CONCERT</span>
    </h1>

    <p class="event-date">07|10|2019</p>
    <p class="event-place">PALMA DE MALLORCA, SPAIN</p>
    <p class="website">WWW.TOMASTUNES.ES</p>
  </main>
</body>
</html>
```